Bag packaging design of sliced bread

The project is for design of line of sliced bread with different flavours. The brand of the bread will be "Valorina". The shape of the bread will be oval. The bread will be packed in a bag. I attach the layout of the bag. The bag will be closed with a plastic clip. I attach images of similar products. The idea is to have one main design and then each colour to be different type of bread like those in the images 2 and 5.

```html
<!DOCTYPE html>
<html lang="en">
<head>
<meta charset="utf-8">
<title>Valorina Organic Bread – Bag Label</title>
<link href="https://fonts.googleapis.com/css2?family=Playfair+Display:wght@600&family=Oswald:wght@300;500&display=swap" rel="stylesheet">
<style>
  :root {
    --backdrop: #e3e3e3;
    --brand-red: #c01d2e;
    --accent-tan: #c9a06e;
    --cream: #f6e9d9;
    --line-red: #c8313f;
  }
  html, body {
    margin: 0;
    padding: 0;
    width: 1000px;
    height: 1200px;
    overflow: hidden;
    background: var(--backdrop);
  }
  .bag-label {
    display: block;
    width: 1000px;
    height: 1200px;
  }
  .brand-name {
    font-family: "Playfair Display", Georgia, serif;
    font-weight: 600;
    font-size: 44px;
    letter-spacing: 1px;
    fill: var(--cream);
  }
  .tagline {
    font-family: "Oswald", Arial, sans-serif;
    font-weight: 500;
    font-size: 11px;
    letter-spacing: 11px;
    fill: var(--cream);
  }
  .claims {
    font-family: "Oswald", Arial, sans-serif;
    font-weight: 300;
    font-size: 13px;
    letter-spacing: 1px;
    fill: var(--cream);
  }
  .flavour-kicker {
    font-family: "Oswald", Arial, sans-serif;
    font-weight: 300;
    font-size: 13px;
    letter-spacing: 6px;
    fill: var(--cream);
  }
  .flavour-name {
    font-family: "Oswald", Arial, sans-serif;
    font-weight: 500;
    font-size: 32px;
    fill: #ffffff;
  }
  .maker-name {
    font-family: "Oswald", Arial, sans-serif;
    font-weight: 500;
    font-size: 11px;
    letter-spacing: 1.5px;
  }
  .maker-name--tan { fill: var(--accent-tan); }
  .maker-name--cream { fill: var(--cream); }
  .net-weight {
    font-family: "Oswald", Arial, sans-serif;
    font-weight: 300;
    font-size: 12px;
    fill: var(--cream);
  }
</style>
</head>
<body>
<svg class="bag-label" viewBox="-351 -74 1250 1500" xmlns="http://www.w3.org/2000/svg">
  <defs>
    <path id="tagline-curve" d="M168,700 Q278,748 392,700"/>
    <path id="claims-curve" d="M146,752 Q278,800 418,752"/>
  </defs>

  <rect class="strap" x="212" y="0" width="126" height="1352" fill="var(--brand-red)"/>

  <path class="band" d="M0,547 Q274,483 548,547 L548,765 Q274,845 0,765 Z" fill="var(--brand-red)"/>

  <g class="outline" fill="none" stroke="var(--accent-tan)" stroke-width="3">
    <path d="M0,535 Q100,511 206,505 L206,0"/>
    <path d="M548,535 Q448,511 344,505 L344,0"/>
    <path d="M0,777 Q100,805 206,813 L206,1352"/>
    <path d="M548,777 Q448,805 344,813 L344,1352"/>
  </g>

  <g class="crest-lines" fill="none" stroke="var(--accent-tan)" stroke-width="2.5">
    <path d="M162,604 L210,584"/>
    <path d="M340,584 L390,604"/>
    <path d="M100,697 Q278,800 455,697"/>
  </g>

  <rect class="wheat wheat--left" x="48" y="580" width="74" height="116" rx="30" fill="#ead7c0" role="img" aria-label="Wheat ear ornament"/>
  <rect class="wheat wheat--right" x="432" y="580" width="74" height="116" rx="30" fill="#ead7c0" role="img" aria-label="Wheat ear ornament"/>

  <g class="maker-mark maker-mark--top">
    <circle cx="276" cy="566" r="10" fill="none" stroke="var(--accent-tan)" stroke-width="2"/>
    <text class="maker-name maker-name--tan" x="276" y="598" text-anchor="middle">HEARTHMILL</text>
  </g>

  <text class="brand-name" x="277" y="678" text-anchor="middle">VALORINA</text>
  <text class="tagline"><textPath href="#tagline-curve" startOffset="50%" text-anchor="middle">ORGANIC BREAD</textPath></text>
  <text class="claims"><textPath href="#claims-curve" startOffset="50%" text-anchor="middle">GMO FREE . TRANCE FAT FREE . GLUTEN FREE</textPath></text>

  <line class="flavour-rule" x1="0" y1="1039" x2="548" y2="1039" stroke="var(--line-red)" stroke-width="1.5"/>
  <rect class="flavour-pill" x="160" y="1015" width="230" height="48" rx="8" fill="var(--brand-red)"/>
  <text class="flavour-kicker" x="278" y="1010" text-anchor="middle">CLASSIC</text>
  <text class="flavour-name" x="275" y="1053" text-anchor="middle">CINNAMON</text>

  <g class="maker-mark maker-mark--bottom">
    <circle cx="275" cy="1205" r="46" fill="none" stroke="var(--accent-tan)" stroke-width="2.5"/>
    <text class="maker-name maker-name--cream" x="275" y="1209" text-anchor="middle">HEARTHMILL</text>
  </g>

  <text class="net-weight" x="275" y="1282" text-anchor="middle">NET WT 18OZ(50g)</text>
</svg>
</body>
</html>
```